Road Construction Company needs business cards

We would like a new business card designed for our business.

We're a road construction company based in Qld, Australia.

Can the business card please have the following information on it.

Name: Brent Malvoy
Position: General Manager
Phone: 0471 592 304
Email: Brent.malvoy@quendix.com.au
Address: 87 Harrowgate Ave, Pindarra, QLD, 4000
Website: www.quendix.com.au

Visually we'd like the card to be professional and simple.

Attached is our logo.

Our website is www.quendix.com.au

Target Market(s)

Men aged 25-60

Contact Information for Business Card

As listed in project description

Font styles to use
Serif

Requirements
Must have
• Large logo on back of card

```html
<!DOCTYPE html>
<html lang="en">
<head>
<meta charset="utf-8">
<title>Quendix Business Card</title>
<link href="https://fonts.googleapis.com/css2?family=Montserrat:wght@600;800&family=Roboto:wght@400&display=swap" rel="stylesheet">
<style>
  :root {
    --stage: #2b2e33;
    --navy: #0a56a8;
    --sky: #2fa6dc;
    --paper: #ffffff;
    --ink: #444a52;
    --muted: #6b7178;
  }
  * { margin: 0; padding: 0; box-sizing: border-box; }
  html, body { width: 1200px; height: 952px; overflow: hidden; }
  body {
    background: var(--stage);
    position: relative;
    font-family: "Roboto", Arial, sans-serif;
  }
  .card {
    position: absolute;
    width: 540px;
    height: 310px;
    overflow: hidden;
    box-shadow: 0 18px 40px rgba(0,0,0,0.45);
  }
  /* Front */
  .card-front { left: 610px; top: 110px; background: var(--paper); }
  .holder { position: absolute; left: 38px; top: 34px; }
  .holder-name {
    font-family: "Montserrat", Arial, sans-serif;
    font-weight: 800;
    font-size: 21px;
    letter-spacing: 0.3px;
    color: var(--navy);
    text-transform: uppercase;
  }
  .holder-role {
    font-family: "Montserrat", Arial, sans-serif;
    font-weight: 600;
    font-size: 11px;
    color: var(--muted);
    margin-top: 3px;
  }
  .holder-rule { width: 62px; height: 2px; background: var(--navy); margin-top: 7px; }
  .contact-list { position: absolute; left: 38px; top: 126px; list-style: none; }
  .contact-item {
    display: flex; align-items: flex-start; gap: 8px;
    font-size: 11.5px; line-height: 15px; color: var(--ink);
    margin-bottom: 7px;
  }
  .contact-icon {
    flex: none; width: 15px; height: 15px; border-radius: 3px;
    background: var(--sky); display: flex; align-items: center; justify-content: center;
  }
  .contact-icon svg { width: 9px; height: 9px; }
  .brand-tab {
    position: absolute; right: 0; top: 168px;
    width: 255px; height: 96px;
    background: var(--sky);
    border-radius: 22px 0 0 22px;
    display: flex; align-items: center; justify-content: center;
  }
  .brand-name {
    font-family: "Montserrat", Arial, sans-serif;
    font-weight: 800;
    color: var(--paper);
    letter-spacing: 2px;
  }
  .brand-tab .brand-name { font-size: 32px; }
  /* Back */
  .card-back { left: 60px; top: 520px; background: var(--navy); }
  .corner-tab { position: absolute; background: var(--sky); width: 120px; height: 74px; }
  .corner-tab.top-left { left: 0; top: 0; border-radius: 0 0 22px 0; }
  .corner-tab.bottom-right { right: 0; bottom: 0; border-radius: 22px 0 0 0; }
  .back-brand {
    position: absolute; inset: 0;
    display: flex; align-items: center; justify-content: center;
  }
  .back-brand .brand-name { font-size: 54px; letter-spacing: 3px; }
</style>
</head>
<body>

  <section class="card card-front" aria-label="Business card front">
    <div class="holder">
      <p class="holder-name">Brent Malvoy</p>
      <p class="holder-role">General Manager</p>
      <div class="holder-rule"></div>
    </div>

    <ul class="contact-list">
      <li class="contact-item">
        <span class="contact-icon"><svg viewBox="0 0 10 10"><path d="M5 0.5a3.2 3.2 0 0 0-3.2 3.2C1.8 6.2 5 9.5 5 9.5s3.2-3.3 3.2-5.8A3.2 3.2 0 0 0 5 0.5zm0 4.5a1.3 1.3 0 1 1 0-2.6 1.3 1.3 0 0 1 0 2.6z" fill="#fff"/></svg></span>
        <span>87 Harrowgate Ave, Pindarra<br>QLD, 4000</span>
      </li>
      <li class="contact-item">
        <span class="contact-icon"><svg viewBox="0 0 10 10"><path d="M2.2 0.8l1.5 1.8-0.9 1.2c0.6 1.3 1.7 2.4 3 3l1.2-0.9 1.8 1.5-0.9 1.6C4.6 8.8 1.2 5.4 0.8 1.7z" fill="#fff"/></svg></span>
        <span>0471 592 304</span>
      </li>
      <li class="contact-item">
        <span class="contact-icon"><svg viewBox="0 0 10 10"><rect x="1" y="2.2" width="8" height="5.6" fill="none" stroke="#fff" stroke-width="1"/><path d="M1 2.4l4 3 4-3" fill="none" stroke="#fff" stroke-width="1"/></svg></span>
        <span>Brent.malvoy@quendix.com.au</span>
      </li>
      <li class="contact-item">
        <span class="contact-icon"><svg viewBox="0 0 10 10"><circle cx="5" cy="5" r="3.8" fill="none" stroke="#fff" stroke-width="1"/><path d="M1.2 5h7.6M5 1.2c-1.6 2.2-1.6 5.4 0 7.6M5 1.2c1.6 2.2 1.6 5.4 0 7.6" fill="none" stroke="#fff" stroke-width="0.8"/></svg></span>
        <span>www.quendix.com.au</span>
      </li>
    </ul>

    <div class="brand-tab">
      <span class="brand-name">QUENDIX</span>
    </div>
  </section>

  <section class="card card-back" aria-label="Business card back">
    <div class="corner-tab top-left"></div>
    <div class="corner-tab bottom-right"></div>
    <div class="back-brand">
      <span class="brand-name">QUENDIX</span>
    </div>
  </section>

</body>
</html>
```